Business Card Design

5* Hotel Property based on an island in Greece

My position is aparta from being a director, i'm on the accounts payable too, not sure how this should be stated, with a comma or "/"?

Sorry about the uploaded logo, it was a mistaken one!

There's also need to be added this  www.corvanteholdings.com on the back side of the card!

Also need to have the logo of the corvante holdings which can be found in a second on the brief! Thank you guys, irini

Industry/Entity Type

Business

Contact Information for Business Card

VERISTOKA PELLA Hotel
Irini Dravetsou
Director, AP Dept.

www.veristoka.gr
Peltira Island 85300
Greece

irinidravetsou@fenmail.com
+306951273064

```html
<!DOCTYPE html>
<html lang="en">
<head>
<meta charset="utf-8">
<title>Veristoka Pella Hotel – Business Card</title>
<link href="https://fonts.googleapis.com/css2?family=Fira+Sans:ital,wght@0,300;0,400;0,500;1,400&display=swap" rel="stylesheet">
<style>
  :root {
    --page: #ffffff;
    --card: #e4e4e4;
    --card-light: #f1f1f1;
    --ink: #16202b;
    --ink-soft: #6a6a6a;
    --blue: #1f6fb8;
    --sea-deep: #1f74c4;
    --sea-mid: #4fb0e6;
    --sea-light: #8fd3f4;
  }
  * { margin: 0; padding: 0; box-sizing: border-box; }
  html, body { width: 1200px; height: 1000px; overflow: hidden; background: var(--page); }
  body { position: relative; font-family: "Fira Sans", "Helvetica Neue", Arial, sans-serif; }

  .card {
    position: absolute;
    left: 319px;
    width: 564px;
    height: 370px;
    overflow: hidden;
    background: radial-gradient(ellipse at 60% 45%, var(--card-light) 0%, var(--card) 65%);
    box-shadow: 4px 6px 14px rgba(0,0,0,0.14);
  }
  .card--front { top: 125px; }
  .card--back { top: 527px; height: 372px; }

  .sea-area {
    position: absolute;
    background: linear-gradient(160deg, var(--sea-deep) 0%, var(--sea-mid) 50%, var(--sea-light) 100%);
  }
  .card--front .sea-area { left: 0; top: 0; width: 120px; height: 100%; }
  .card--back .sea-area { left: 0; top: 120px; width: 120px; height: 252px;
    background: linear-gradient(20deg, var(--sea-deep) 0%, var(--sea-mid) 55%, var(--sea-light) 100%); }

  .brand { position: absolute; display: flex; align-items: center; }
  .brand__dot { border-radius: 50%; background: var(--sea-mid); flex: none; }
  .brand__name { font-weight: 300; color: var(--ink-soft); line-height: 1.05; white-space: nowrap; }
  .brand__name span { display: block; }

  .card--front .brand { left: 135px; top: 43px; gap: 14px; }
  .card--front .brand__dot { width: 64px; height: 64px; }
  .card--front .brand__name { font-size: 20px; }
  .card--front .brand__name span { font-size: 13px; letter-spacing: 6px; margin-top: 2px; }

  .card--back .brand { left: 93px; top: 135px; gap: 16px; }
  .card--back .brand__dot { width: 100px; height: 100px; }
  .card--back .brand__name { font-size: 31px; }
  .card--back .brand__name span { font-size: 19px; letter-spacing: 10px; margin-top: 4px; }

  .details { position: absolute; left: 192px; top: 123px; }
  .details__name {
    font-size: 22px; font-weight: 400; letter-spacing: 5px; line-height: 28px;
    color: var(--ink); text-transform: uppercase; white-space: nowrap;
  }
  .details__role { margin-top: 1px; font-size: 14.5px; line-height: 20px; color: var(--blue); letter-spacing: 0.3px; }
  .details__address { margin-top: 22px; font-size: 15px; line-height: 20px; font-style: italic; color: var(--ink); white-space: nowrap; }
  .contact { margin-top: 13px; list-style: none; font-size: 13.5px; }
  .contact li { display: flex; align-items: center; gap: 5px; height: 24px; white-space: nowrap; }
  .contact__label { color: var(--blue); }
  .contact__value { color: var(--ink); }
  .contact svg { flex: none; }
  .details__web { display: block; font-size: 13.5px; line-height: 24px; color: var(--blue); text-decoration: none; }

  .group-web {
    position: absolute; right: 26px; bottom: 18px;
    font-size: 12px; color: var(--blue); text-decoration: none; letter-spacing: 0.3px;
  }
</style>
</head>
<body>

<section class="card card--front" aria-label="Business card front">
  <div class="sea-area" role="img" aria-label="Illustrated blue sea along the left edge"></div>

  <div class="brand">
    <span class="brand__dot"></span>
    <p class="brand__name">VERISTOKA PELLA<span>HOTEL</span></p>
  </div>

  <div class="details">
    <h1 class="details__name">Irini Dravetsou</h1>
    <p class="details__role">DIRECTOR &nbsp;|&nbsp; AP DEPT.</p>
    <p class="details__address">Peltira Island 85300, Greece</p>
    <ul class="contact">
      <li>
        <svg width="16" height="12" viewBox="0 0 16 12" aria-hidden="true"><rect x="0.5" y="0.5" width="15" height="11" fill="none" stroke="var(--blue)"/><path d="M0.5 0.5 L8 7 L15.5 0.5" fill="none" stroke="var(--blue)"/></svg>
        <span class="contact__label">email :</span>
        <span class="contact__value">irinidravetsou@fenmail.com</span>
      </li>
      <li>
        <svg width="14" height="14" viewBox="0 0 14 14" aria-hidden="true"><rect width="14" height="14" rx="2" fill="var(--blue)"/><path d="M4 3 C3 5 5 10 10 11 L11 9.5 L9 8.5 L8 9.3 C6.5 8.5 5.5 7.5 4.8 6 L5.6 5 L4.7 3 Z" fill="#fff"/></svg>
        <span class="contact__label">&nbsp;telephone :</span>
        <span class="contact__value">+306951273064</span>
      </li>
    </ul>
    <a class="details__web" href="#">www.veristoka.gr</a>
  </div>
</section>

<section class="card card--back" aria-label="Business card back">
  <div class="sea-area" role="img" aria-label="Illustrated blue sea in the lower left corner"></div>

  <div class="brand">
    <span class="brand__dot"></span>
    <p class="brand__name">VERISTOKA PELLA<span>HOTEL</span></p>
  </div>

  <a class="group-web" href="#">www.corvanteholdings.com</a>
</section>

</body>
</html>
```